Premium stylish simple clever card design for high end construction company.

I need a business card designed that is a standard size and shape (square edges) that is black in colour, with black edges. All text is to be either grey/silver or yellow/gold. On the front I want the logo (supplied as attachment g5) to be embossed or raised to give a texture. I also want the name of my company "The Kestrel Vault (larger font) construction co. (smaller font)" I like the clean style (found in attachment 56419286) of the black background with silver text. But the triangle is to be gold/yellow.

On the back needs to have my contact details. In silver or gold text.

Liam Porter - Builder
Liam@thekestrelvault.com.au
www.thekestrelvault.com.au
0427391065
Lic 517904k
PO BOX 739 Tallowmere NSW 2188

Must look simple, elegant and precise.

My work is of the utmost quality and my business card needs to project that. It needs to be simple and precise. It should scream luxury and confidence. Feel free to get creative with the font and font size. If you google "The Kestrel Vault" you will see it has links to great architecture, art, nature and the fibonacci sequence so i am open to using these ideas also.

Target Market(s)

High End home owners. 30-70 year olds.

Industry/Entity Type

Residential Construction

Contact Information for Business Card

Logo and company name on front. Contact details on back.

Font styles to use
Serif
Sans Serif

Colors
ffcf3e

Requirements
Must have
• black background
Nice to have
• debossed logo (silver and gold)
• debased company name (silver)
Should not have
• It should not look like a standard construction business card with pictures of hammers or tools etc.

```html
<!DOCTYPE html>
<html lang="en">
<head>
<meta charset="utf-8">
<title>The Kestrel Vault – Business Card</title>
<link href="https://fonts.googleapis.com/css2?family=Questrial&display=swap" rel="stylesheet">
<style>
  :root {
    --backdrop: #d6d6d6;
    --card: #0c0c0c;
    --card-edge: #050505;
    --silver: #b9b9b9;
    --silver-dim: #8a8a8a;
    --rule: #6d6d6d;
    --gold: #ffcf3e;
    --gold-deep: #c9a227;
    --font-main: "Questrial", "Century Gothic", sans-serif;
  }
  * { margin: 0; padding: 0; box-sizing: border-box; }
  html, body {
    width: 1000px;
    height: 1200px;
    overflow: hidden;
    background: var(--backdrop);
    font-family: var(--font-main);
  }
  .sheet {
    position: relative;
    width: 1000px;
    height: 1200px;
  }
  .card {
    position: absolute;
    left: 100px;
    width: 800px;
    height: 457px;
    background: linear-gradient(135deg, #151515 0%, var(--card) 55%, #080808 100%);
    border: 1px solid var(--card-edge);
    box-shadow: 0 10px 28px rgba(0,0,0,0.35);
    overflow: hidden;
  }
  .card--front { top: 110px; }
  .card--back { top: 633px; }

  /* Front */
  .front-brand {
    position: absolute;
    left: 50%;
    top: 50%;
    transform: translate(-50%, -50%);
    display: flex;
    align-items: center;
    gap: 20px;
    white-space: nowrap;
  }
  .brand-dot {
    width: 54px;
    height: 54px;
    border-radius: 50%;
    background: var(--silver-dim);
    flex: none;
  }
  .brand-text { display: flex; flex-direction: column; flex: none; }
  .brand-name {
    color: var(--silver);
    font-size: 38px;
    font-weight: 400;
    letter-spacing: 2px;
    text-transform: uppercase;
    line-height: 1.1;
    padding-bottom: 6px;
    border-bottom: 1px solid var(--rule);
    white-space: nowrap;
  }
  .brand-sub {
    color: var(--silver-dim);
    font-size: 12px;
    letter-spacing: 3px;
    text-transform: uppercase;
    text-align: right;
    margin-top: 5px;
    white-space: nowrap;
  }

  /* Back */
  .back-brand {
    position: absolute;
    left: 48px;
    top: 42px;
    display: flex;
    align-items: center;
    gap: 14px;
    white-space: nowrap;
  }
  .back-brand .brand-dot { width: 34px; height: 34px; }
  .back-brand .brand-name { font-size: 24px; letter-spacing: 1px; padding-bottom: 3px; }
  .back-brand .brand-sub { font-size: 8px; letter-spacing: 2px; margin-top: 3px; }

  .holder {
    position: absolute;
    right: 60px;
    top: 150px;
    text-align: right;
    white-space: nowrap;
  }
  .holder-name {
    color: var(--gold);
    font-size: 30px;
    letter-spacing: 1.5px;
    text-transform: uppercase;
  }
  .holder-role {
    color: var(--silver);
    font-size: 18px;
    margin-top: 2px;
  }

  .contact {
    position: absolute;
    left: 48px;
    bottom: 44px;
    color: var(--silver);
    font-size: 17px;
    letter-spacing: 0.6px;
    line-height: 1.35;
    list-style: none;
    white-space: nowrap;
  }
  .contact-line { display: flex; align-items: center; gap: 10px; }
  .contact-icon { width: 15px; height: 15px; flex: none; }
  .contact-gap { margin-top: 16px; }
</style>
</head>
<body>
<main class="sheet">

  <section class="card card--front" aria-label="Card front">
    <div class="front-brand">
      <span class="brand-dot" aria-hidden="true"></span>
      <div class="brand-text">
        <h1 class="brand-name">The Kestrel Vault</h1>
        <p class="brand-sub">Construction Co.</p>
      </div>
    </div>
  </section>

  <section class="card card--back" aria-label="Card back">
    <div class="back-brand">
      <span class="brand-dot" aria-hidden="true"></span>
      <div class="brand-text">
        <p class="brand-name">The Kestrel Vault</p>
        <p class="brand-sub">Construction Co.</p>
      </div>
    </div>

    <div class="holder">
      <p class="holder-name">Liam Porter</p>
      <p class="holder-role">Builder</p>
    </div>

    <ul class="contact">
      <li class="contact-line">
        <svg class="contact-icon" viewBox="0 0 16 16" aria-hidden="true">
          <rect x="1" y="1" width="14" height="14" rx="2" fill="var(--gold-deep)"/>
          <path d="M5 4h2l1 3-1.3 1a6 6 0 0 0 2.3 2.3L10 9l3 1v2a1 1 0 0 1-1 1A8 8 0 0 1 4 5a1 1 0 0 1 1-1z" fill="var(--card)"/>
        </svg>
        <span>042 7391 065</span>
      </li>
      <li class="contact-line">
        <svg class="contact-icon" viewBox="0 0 16 16" aria-hidden="true">
          <rect x="1" y="3" width="14" height="10" fill="var(--gold-deep)"/>
          <path d="M1 3l7 6 7-6" fill="none" stroke="var(--card)" stroke-width="1.4"/>
        </svg>
        <span>Liam@thekestrelvault.com.au</span>
      </li>
      <li class="contact-line">
        <svg class="contact-icon" viewBox="0 0 16 16" aria-hidden="true">
          <circle cx="8" cy="8" r="7" fill="var(--gold-deep)"/>
          <g fill="none" stroke="var(--card)" stroke-width="1">
            <ellipse cx="8" cy="8" rx="3" ry="7"/>
            <line x1="1" y1="8" x2="15" y2="8"/>
          </g>
        </svg>
        <span>www.thekestrelvault.com.au</span>
      </li>
      <li class="contact-line contact-gap"><span>PO BOX 739 Tallowmere NSW 2188</span></li>
      <li class="contact-line"><span>Lic 517904k</span></li>
    </ul>
  </section>

</main>
</body>
</html>
```